BRW (Miriela Vondrash Wellness) Website supporting women to live a healthy lifestyle

Hi
I'm thrilled to be working together to bring a fresh look to my website! As an Integrative Health Practitioner, my mission is to support and empower women on their journey to reclaim their health and well-being. The website should feel inviting, with a soft and nurturing energy that also radiates vibrancy and vitality.

Design & Aesthetic:

I'd love to focus on rich rose gold tones
It should feel soft and approachable yet energetic and lively.

Functional Needs:

The site will support both my coaching services
and product sales, so it’s essential to have an intuitive and user-friendly shopping experience.
I'd love some exciting interactive features that keep visitors engaged and make the journey through the site feel seamless and uplifting.

Please let me know if there’s any additional information you need from me to bring this vision to life!

Thank you for your attention to these details! Here are some ideas I like to see Layout Ideas

Hero Section: An inviting header with a subtle half-moon background for a touch of healing energy.

Navigation & Logo: Place my logo in gold on the top left and use simple navigation links with a rose gold hover effect.

Section Dividers: Use small celestial icons, like a crescent moon, as dividers to create flow and add a bit of magic.

Product & Service Section: A soft rose gold gradient background to highlight products, with circular or wave accents around images.

Footer: Deep rose gold background with a half-moon icon to end with a warm invitation to connect.

Uploading an AI-generated image (it is a bit over the top but it captures the feel I like), with a hint of spirituality and femininity, along with elements like the half moon and colors. :) I'm also uploading my logos, and I have each option available in both color schemes.

Best,
Miriela

• Playfair Display (Headings) & Lora (Body Text)

• Cartwell

```html
<!DOCTYPE html>
<html lang="en">
<head>
<meta charset="utf-8">
<title>BRW – Miriela Vondrash Wellness</title>
<link rel="stylesheet" href="https://fonts.googleapis.com/css2?family=Playfair+Display:wght@700;900&family=Lora:wght@400;700&display=swap">
<style>
:root{
  --rose:#e9a98a;
  --rose-deep:#e3a27f;
  --rose-light:#f6c9ad;
  --blush:#f8d3d3;
  --gold-line:#d9a48a;
  --ink:#1c1b1b;
  --text:#4a4440;
  --white:#ffffff;
}
*{margin:0;padding:0;box-sizing:border-box}
html,body{width:1200px;height:3964px;overflow:hidden;background:var(--white)}
body{position:relative;font-family:'Lora',serif;color:var(--text)}
.abs{position:absolute}
.heading{font-family:'Playfair Display',serif;font-weight:700;color:var(--ink);text-transform:uppercase;letter-spacing:.3px}
.squiggle{display:block}
.btn-outline{position:absolute;border:2px solid var(--rose);border-radius:30px;color:var(--rose);font-family:'Lora',serif;font-size:13px;text-transform:uppercase;display:flex;align-items:center;justify-content:center;background:var(--white)}
.logo-badge{position:absolute;border-radius:50%;background:var(--white);border:2px solid var(--gold-line);display:flex;align-items:center;justify-content:center;font-family:'Playfair Display',serif;font-weight:700;color:var(--rose-deep)}
.media{position:absolute;overflow:hidden}
.nav{left:200px;top:55px;width:910px;height:90px;background:var(--white);border-radius:45px;box-shadow:0 6px 20px rgba(200,140,120,.15);display:flex;align-items:center;padding-left:124px}
.nav a{font-size:14px;color:var(--ink);text-decoration:none;text-transform:uppercase;padding:0 22px;border-left:1px solid #ccc;line-height:16px}
.nav a:first-child{border-left:none;color:var(--rose)}
.nav .nav-cta{margin-left:8px;border:none;background:linear-gradient(90deg,#f0b08c,#e7a07c);color:var(--white);border-radius:26px;padding:14px 20px;font-size:13px}
.program-icon{position:absolute;width:78px;height:78px;border-radius:50%;background:linear-gradient(135deg,#f2b594,#e39b78);display:flex;align-items:center;justify-content:center;box-shadow:0 6px 14px rgba(227,155,120,.35)}
.program-label{position:absolute;font-family:'Playfair Display',serif;font-weight:700;font-size:17px;color:var(--ink);text-transform:uppercase}
.card{position:absolute;top:2187px;width:245px;height:331px;background:var(--white);border-radius:12px;overflow:hidden}
.card .media{left:0;top:0;width:245px;height:190px;position:absolute}
.card h3{position:absolute;left:30px;top:212px;font-family:'Playfair Display',serif;font-weight:700;font-size:16px;line-height:22px;color:var(--ink);text-transform:uppercase}
.card p{position:absolute;left:30px;top:268px;width:190px;font-size:12.5px;line-height:17px;color:var(--text)}
.quote{position:absolute;top:2870px;width:340px}
.quote .marks{position:absolute;left:-88px;top:-50px;font-family:'Playfair Display',serif;font-size:170px;line-height:1;color:#fbe6dc}
.quote p{position:relative;font-size:16px;line-height:24px;color:var(--text)}
.quote .who{position:relative;margin-top:24px;font-family:'Playfair Display',serif;font-weight:700;font-size:14px;color:var(--ink)}
.dots{position:absolute;display:flex;gap:8px}
.dots span{width:9px;height:9px;border-radius:50%;background:#f5d5c7}
.dots span.on{background:var(--rose)}
.footer-link{position:absolute;top:3766px;font-size:17px;color:var(--white)}
</style>
</head>
<body>

<svg class="abs" style="left:0;top:0" width="1200" height="860" viewBox="0 0 1200 860">
  <defs>
    <linearGradient id="heroWash" x1="0" y1="0" x2="1" y2="1">
      <stop offset="0" stop-color="#fbe3e3"/>
      <stop offset=".5" stop-color="#f7c9cc"/>
      <stop offset="1" stop-color="#f9d6cf"/>
    </linearGradient>
  </defs>
  <path d="M0 0H1200V760C1100 800 980 790 860 740C720 680 640 600 480 610C300 620 160 690 0 670Z" fill="url(#heroWash)"/>
</svg>

<div class="media" role="img" aria-label="Woman in grey activewear meditating cross-legged with hands in prayer, framed by a half-moon and line-drawn leaves" style="left:600px;top:250px;width:430px;height:550px;border-radius:215px 215px 40px 40px;background:linear-gradient(180deg,#efe4e2 0%,#cdc4c4 55%,#bdb6b6 100%)"></div>

<nav class="abs nav">
  <a href="#">Home</a><a href="#">Programs</a><a href="#">Labs</a><a href="#">About</a><a href="#">Testimonials</a>
  <a href="#" class="nav-cta">Claim your free consult!</a>
</nav>
<div class="logo-badge" style="left:88px;top:33px;width:134px;height:134px;font-size:38px">BRW</div>

<h1 class="abs heading" style="left:88px;top:268px;font-size:54px;line-height:62px">Achieve peak<br>health,<br>productivity</h1>
<p class="abs heading" style="left:88px;top:468px;font-size:20px">And energy with zero stress</p>

<h2 class="abs heading" style="left:0;width:1200px;top:870px;text-align:center;font-size:36px">What my programs include:</h2>
<svg class="abs squiggle" style="left:575px;top:925px" width="50" height="12" viewBox="0 0 50 12"><path d="M2 8Q8 0 14 8T26 8T38 8T50 8" fill="none" stroke="var(--rose)" stroke-width="2"/></svg>
<p class="abs" style="left:250px;width:700px;top:952px;text-align:center;font-size:15px;line-height:24px">*my programs are not intended to treat, prevent or cure disease. Rather, rebalance the underlying root causes &amp; support the body in achieving its best health!</p>

<div class="abs" style="left:470px;top:1025px;width:260px;height:260px;border-radius:50%;background:var(--white);box-shadow:0 0 40px rgba(220,170,150,.25)"></div>
<div class="logo-badge" style="left:515px;top:1070px;width:170px;height:170px;font-size:52px;border:none">BRW</div>

<div class="program-icon" style="left:429px;top:1033px"><svg width="38" height="38" viewBox="0 0 38 38" fill="none" stroke="#fff" stroke-width="2"><rect x="5" y="7" width="28" height="20" rx="2"/><circle cx="19" cy="15" r="3"/><path d="M14 23Q19 17 24 23M12 31H26"/></svg></div>
<div class="program-icon" style="left:685px;top:1033px"><svg width="38" height="38" viewBox="0 0 38 38" fill="none" stroke="#fff" stroke-width="2"><circle cx="19" cy="19" r="11"/><path d="M6 20V15M32 20V15M14 19H15M19 19H20M24 19H25"/></svg></div>
<div class="program-icon" style="left:429px;top:1194px"><svg width="38" height="38" viewBox="0 0 38 38" fill="none" stroke="#fff" stroke-width="2"><rect x="7" y="6" width="20" height="26" rx="2"/><path d="M11 13H23M11 18H21M11 23H17"/><circle cx="27" cy="27" r="5"/></svg></div>
<div class="program-icon" style="left:685px;top:1194px"><svg width="38" height="38" viewBox="0 0 38 38" fill="none" stroke="#fff" stroke-width="2"><rect x="6" y="15" width="20" height="10" rx="5" transform="rotate(-35 16 20)"/><circle cx="27" cy="24" r="6"/></svg></div>

<div class="program-label" style="left:258px;top:1061px">Zoom consults</div>
<div class="program-label" style="left:783px;top:1061px">Lifestyle support</div>
<div class="program-label" style="left:296px;top:1223px">Lab testing</div>
<div class="program-label" style="left:783px;top:1223px">Supplements</div>

<div class="btn-outline" style="left:508px;top:1335px;width:183px;height:44px">View programs</div>

<svg class="abs" style="left:0;top:1780px" width="1200" height="900" viewBox="0 0 1200 900">
  <defs>
    <linearGradient id="peach" x1="0" y1="0" x2="0" y2="1">
      <stop offset="0" stop-color="#eaa585"/>
      <stop offset=".5" stop-color="#f4bc9a"/>
      <stop offset="1" stop-color="#e9aa8a"/>
    </linearGradient>
  </defs>
  <path d="M0 90C150 20 300 60 430 140C600 230 800 230 1000 170C1100 140 1160 100 1200 80V750C1100 790 980 830 800 790C620 750 520 810 380 850C250 890 120 890 0 860Z" fill="url(#peach)"/>
</svg>

<div class="abs" style="left:122px;top:1438px;width:456px;height:456px;border-radius:50%;border:2px solid var(--gold-line);background:var(--white)"></div>
<div class="media" role="img" aria-label="Tired woman in white shirt holding her hand to her forehead" style="left:140px;top:1456px;width:420px;height:420px;border-radius:50%;background:linear-gradient(160deg,#e7e7ea 0%,#c9c9cf 50%,#b79f86 100%)"></div>
<div class="abs" style="left:435px;top:1792px;width:92px;height:92px;border-radius:50%;background:var(--white);box-shadow:0 4px 14px rgba(0,0,0,.12);display:flex;align-items:center;justify-content:center">
  <svg width="26" height="26" viewBox="0 0 26 26"><path d="M7 4L22 13L7 22Z" fill="var(--rose)"/></svg>
</div>

<h2 class="abs heading" style="left:616px;top:1470px;font-size:36px">A success story</h2>
<svg class="abs squiggle" style="left:616px;top:1526px" width="46" height="12" viewBox="0 0 46 12"><path d="M2 8Q8 0 14 8T26 8T38 8T46 8" fill="none" stroke="var(--rose)" stroke-width="2"/></svg>
<div class="abs" style="left:616px;top:1555px;width:470px;font-size:14.5px;line-height:20px;color:var(--text)">
  <p>When we started working together, she was experiencing:</p>
  <p style="margin-top:20px"><b>1. GullBladder Attacks</b> -carrying pain medication everywhere</p>
  <p style="margin-top:14px"><b>2. No Energy</b>- yet working ridiculous work hours</p>
  <p style="margin-top:14px">She also had <b>seen other Naturopaths</b>; yet she continued to simply be given <b>supplements &amp; medication</b>. To the point where she was <b>scheduled to have a surgery!</b></p>
  <p style="margin-top:14px">She is a perfect example of the power of Integrative Health and how possible it is to change your quality of life altogether.</p>
</div>
<div class="btn-outline" style="left:616px;top:1812px;width:272px;height:44px">Claim your free consult!</div>

<h2 class="abs heading" style="left:0;width:1200px;top:2046px;text-align:center;font-size:36px;color:var(--white)">What is integrative health?</h2>
<svg class="abs squiggle" style="left:577px;top:2101px" width="46" height="12" viewBox="0 0 46 12"><path d="M2 8Q8 0 14 8T26 8T38 8T46 8" fill="none" stroke="#fff" stroke-width="2"/></svg>
<p class="abs" style="left:0;width:1200px;top:2128px;text-align:center;font-size:15px;color:#fff7f2">Integrative health coaching brings together</p>

<div class="card" style="left:89px"><div class="media" role="img" aria-label="Mortar and pestle with herbs and spices" style="background:linear-gradient(135deg,#f3efe9,#6b8a4c 55%,#c9802f)"></div><h3>Ayurvedic<br>medicine</h3><p>The Science of Life</p></div>
<div class="card" style="left:348px"><div class="media" role="img" aria-label="Soft grey DNA helix" style="background:linear-gradient(135deg,#d6d6d6,#b8b8b8)"></div><h3>Bioregulatory<br>medicine</h3><p>The Science of Self-Healing. Traditional Chinese</p></div>
<div class="card" style="left:607px"><div class="media" role="img" aria-label="Glass cup of green herbal tea with leaves" style="background:linear-gradient(135deg,#c9c9c6,#a7b23e 55%,#8a8a84)"></div><h3>Medicine and<br>herbalism</h3><p>Using the power of herbs and energy practice to enhance.</p></div>
<div class="card" style="left:866px"><div class="media" role="img" aria-label="Silhouette profile with glowing brain energy" style="background:linear-gradient(135deg,#f6f6f6 30%,#25476b 60%,#d8782a)"></div><h3>Eastern<br>philosophy</h3><p>Using the Mind to Heal the Body.</p></div>

<div class="dots" style="left:586px;top:2563px"><span class="on"></span><span style="background:#f8d8c6"></span></div>

<h2 class="abs heading" style="left:0;width:1200px;top:2664px;text-align:center;font-size:36px;line-height:44px">What our client<br>others say</h2>
<svg class="abs squiggle" style="left:577px;top:2763px" width="46" height="12" viewBox="0 0 46 12"><path d="M2 8Q8 0 14 8T26 8T38 8T46 8" fill="none" stroke="var(--rose)" stroke-width="2"/></svg>

<div class="quote" style="left:172px"><div class="marks">&ldquo;</div><p>Miriela is a passionate health mentor who genuinely cares about her clients and is generous with her time and knowledge. Her authentic, skilled, compassionate nature makes her an absolute joy to work with.</p><div class="who">– ROSALIND</div></div>
<div class="quote" style="left:630px"><div class="marks">&ldquo;</div><p>Miriela is practical but also realistic. Setting small achievable easy understanding lifestyle changes was important to get started with making change. Miriela provided a list of healthy changes resulting from feedback.</p><div class="who">– TOBIN</div></div>
<div class="quote" style="left:1090px"><div class="marks">&ldquo;</div><p>I am SO happy with the results! New food I make is now a joy. Everything just feels lighter and so much better, more focus, more energy, better sleep.</p><div class="who">– ILSE</div></div>

<div class="dots" style="left:566px;top:3084px"><span></span><span class="on"></span><span></span></div>

<svg class="abs" style="left:0;top:3140px" width="1200" height="824" viewBox="0 0 1200 824">
  <defs>
    <linearGradient id="footerGrad" x1="0" y1="0" x2="0" y2="1">
      <stop offset="0" stop-color="#f2b999"/>
      <stop offset="1" stop-color="#eaa886"/>
    </linearGradient>
  </defs>
  <path d="M0 440C200 520 420 500 620 420C800 350 1000 300 1200 330V824H0Z" fill="url(#footerGrad)"/>
</svg>

<div class="media" role="img" aria-label="Woman with long braids in a blush top meditating in lotus pose, framed by a half-moon and line-drawn leaves" style="left:560px;top:3140px;width:440px;height:470px;border-radius:220px 220px 40px 40px;background:linear-gradient(180deg,#f3e2da 0%,#d7bfb2 45%,#4c4a55 100%)"></div>

<h2 class="abs heading" style="left:143px;top:3176px;font-size:36px;line-height:45px">Are you ready to feel<br>the best you have<br>ever felt?</h2>
<svg class="abs squiggle" style="left:143px;top:3322px" width="46" height="12" viewBox="0 0 46 12"><path d="M2 8Q8 0 14 8T26 8T38 8T46 8" fill="none" stroke="var(--rose)" stroke-width="2"/></svg>
<p class="abs heading" style="left:143px;top:3350px;font-size:16px">Book a free consult with me here:</p>
<div class="btn-outline" style="left:143px;top:3400px;width:272px;height:44px">Claim your free consult!</div>

<div class="logo-badge" style="left:148px;top:3690px;width:160px;height:160px;font-size:46px;border:none">BRW</div>
<div class="abs" style="left:371px;top:3745px;width:252px;height:62px;border-radius:31px;background:rgba(255,255,255,.22);display:flex;align-items:center;justify-content:center;gap:8px;color:#fff;font-size:18px;font-weight:700">
  <svg width="20" height="16" viewBox="0 0 20 16"><rect x="1" y="1" width="18" height="14" rx="2" fill="#fff"/><path d="M1 2L10 9L19 2" fill="none" stroke="#eaa886" stroke-width="1.6"/></svg>
  hello@brwellness.au
</div>
<span class="footer-link" style="left:684px">Privacy</span>
<span class="footer-link" style="left:772px">Terms &amp; Conditions</span>
<span class="footer-link" style="left:965px">Disclaimer</span>
<div class="abs" style="left:1130px;top:3870px;width:40px;height:40px;border-radius:50%;background:#fff;display:flex;align-items:center;justify-content:center">
  <svg width="14" height="14" viewBox="0 0 14 14"><path d="M3 9L7 5L11 9" fill="none" stroke="var(--rose)" stroke-width="2"/></svg>
</div>
<p class="abs" style="left:0;width:1200px;top:3920px;text-align:center;font-size:14px;color:#fff">© COPYRIGHT 2024 MYBRW. ALL RIGHTS RESERVED</p>

</body>
</html>
```